The Corvane Agency

We are a pr, social media and strategy agency specializing in the pet industry. We would like a new dynamic design of our existing website. We think it is currently outdated and looks too corporate. We would like it to look more consumer oriented as we primarily market pet products. We would like warm imagery involving pets and while pets are fun, this is still a business website and needs to maintain a professional look. We are hired by business owners and executives.
I would like some of our work featured on the home page.
Our primary service tabs are:
Public Relations
Social Media
Product Consulting
Most of the content will remain the same but we are open to suggestions!
Our current website can be found at www.corvanepetpr.example.
We are open to other colors than in our logo and on our current page.
This is a design only project and will not require programming. The selected designer will need to provide at least one interior page in addition to the home page.

Industry/Entity Type

Pet

Requirements
Should not have
• Cartoon type figures. Pet puns.

```html
<!DOCTYPE html>
<html lang="en">
<head>
<meta charset="utf-8">
<title>The Corvane Agency</title>
<link href="https://fonts.googleapis.com/css2?family=Open+Sans:ital,wght@0,300;0,400;0,600;0,700;1,400&display=swap" rel="stylesheet">
<style>
:root{
  --red:#d7232f;
  --ink:#333333;
  --muted:#777777;
  --light:#f1f1f1;
  --card:#e3e3e3;
  --tab:#3a3a3a;
  --tab-active:#1f1f1f;
  --footer:#2b2b2b;
  --footer-deep:#1c1c1c;
  --footer-text:#9a9a9a;
  --white:#ffffff;
}
*{box-sizing:border-box;margin:0;padding:0}
html,body{width:769px;height:1200px;overflow:hidden}
body{font-family:"Open Sans",Arial,sans-serif;color:var(--ink);background:var(--white)}
section,header,footer{overflow:hidden}
.site-header{height:34px;display:flex;align-items:center;justify-content:space-between;padding:0 60px;background:var(--white);border-bottom:1px solid #eee}
.brand{display:flex;align-items:center;gap:6px;color:var(--red);font-weight:700;font-size:14px}
.brand-dot{width:10px;height:10px;border-radius:50%;background:var(--red)}
.main-nav{display:flex;height:100%}
.main-nav a{display:flex;align-items:center;padding:0 9px;font-size:8px;color:var(--ink);text-decoration:none;font-weight:600}
.main-nav a.active{background:var(--red);color:var(--white)}
.hero{position:relative;height:240px;background:radial-gradient(circle at 70% 45%,#e9d2a6 0,#d9a45a 35%,#c6802e 65%,#8f5a22 100%)}
.hero-media{position:absolute;inset:0}
.hero-copy{position:absolute;left:95px;top:34px;width:200px}
.hero-copy .lead{font-size:22px;font-weight:700;color:var(--red);line-height:1.1}
.hero-copy .title{font-size:22px;font-weight:700;color:var(--ink);line-height:1.15}
.hero-copy p{font-size:7.5px;line-height:1.5;margin:8px 0 10px;color:#3e3e3e}
.btn{display:inline-block;background:var(--red);color:var(--white);font-size:7px;font-weight:600;padding:5px 12px;border-radius:2px}
.hero-dots{position:absolute;bottom:10px;left:50%;transform:translateX(-50%);display:flex;gap:5px}
.hero-dots span{width:6px;height:6px;border-radius:50%;background:rgba(255,255,255,.6)}
.hero-dots span.on{background:var(--red)}
.section-title{text-align:center;font-weight:300;font-size:25px;line-height:1.3;color:var(--ink)}
.section-sub{text-align:center;font-size:8px;color:var(--muted);margin-top:4px}
.functions{padding-top:22px;height:304px}
.cards{display:flex;justify-content:center;align-items:flex-end;gap:6px;margin-top:24px}
.card{width:158px;height:133px;background:var(--card);text-align:center;padding:12px 14px 0}
.card.featured{background:var(--red);color:var(--white);height:145px;padding-top:18px}
.card-icon{width:34px;height:34px;border-radius:50%;margin:0 auto 6px;display:flex;align-items:center;justify-content:center;background:var(--white)}
.card:not(.featured) .card-icon{background:transparent}
.card h3{font-size:9px;font-weight:700;margin-bottom:4px}
.card p{font-size:6.5px;line-height:1.45;margin-bottom:7px}
.card .btn{background:var(--white);color:var(--red)}
.card:not(.featured) .btn{background:var(--red);color:var(--white)}
.experts{height:182px;padding-top:12px}
.experts-text{width:620px;margin:6px auto 0;font-size:7px;line-height:1.6;text-align:center;color:var(--muted)}
.tabs{width:625px;margin:14px auto 0;display:flex;background:var(--tab)}
.tabs span{flex:1;font-size:7px;color:#ddd;text-align:center;padding:6px 0;border-right:1px solid #555}
.tabs span.active{background:var(--tab-active);color:var(--white);font-weight:700}
.tab-panel{width:625px;margin:0 auto;height:56px;background:var(--light);display:flex;justify-content:space-between}
.tab-panel p{width:470px;padding:7px 14px;font-size:7px;line-height:1.55;color:var(--muted)}
.tab-photo{width:125px;height:56px;background:linear-gradient(135deg,#cfc0a6,#a08566)}
.team{padding-top:4px;height:225px}
.team-row{position:relative;display:flex;justify-content:center;gap:22px;margin-top:8px}
.member{width:86px;text-align:center}
.member-photo{height:86px;background:linear-gradient(180deg,#e3ddd6,#b9aea2)}
.member h4{font-size:7.5px;font-weight:600;margin-top:5px;line-height:1.3}
.member span{display:block;font-size:6.5px;color:var(--red);line-height:1.4}
.arrow{position:absolute;top:36px;width:16px;height:16px;border-radius:50%;background:#bbb}
.arrow.prev{left:88px}
.arrow.next{right:88px}
.testimonial{width:625px;margin:14px auto 0;height:36px;background:var(--light);display:flex;align-items:center;gap:12px;padding:0 14px}
.testimonial-photo{width:26px;height:26px;border-radius:50%;background:#b9a08a;flex:none}
.testimonial p{font-size:6.8px;font-style:italic;color:var(--muted);line-height:1.5}
.site-footer{height:195px;background:var(--footer);display:flex;gap:22px;padding:18px 60px 0}
.footer-col h5{font-size:7.5px;color:var(--white);font-weight:600;margin-bottom:7px}
.footer-col li{list-style:none;font-size:6px;color:var(--footer-text);line-height:1.75}
.col-narrow{width:80px}
.col-blog{width:120px}
.footer-map{width:85px;height:52px;background:linear-gradient(135deg,#d8d8d0,#b9c0b0)}
.footer-phone{font-size:13px;color:var(--white);font-weight:300;margin-top:6px}
.gallery{display:grid;grid-template-columns:repeat(3,30px);gap:3px}
.gallery span{height:26px;background:linear-gradient(135deg,#8b6f57,#c29f78)}
.footer-bar{height:20px;background:var(--footer-deep);display:flex;justify-content:space-between;align-items:center;padding:0 60px}
.footer-bar small{font-size:6px;color:var(--footer-text)}
.social{display:flex;gap:3px}
.social span{width:9px;height:9px;background:#555}
</style>
</head>
<body>
<header class="site-header">
  <div class="brand"><span class="brand-dot"></span>The Corvane Agency</div>
  <nav class="main-nav">
    <a href="#">PR</a>
    <a href="#" class="active">Social Media</a>
    <a href="#">Product Consulting</a>
    <a href="#">Pet Experts</a>
    <a href="#">Our Team</a>
    <a href="#">Contact Us</a>
  </nav>
</header>

<section class="hero">
  <div class="hero-media" role="img" aria-label="Photo of a small dog sitting in warm autumn light"></div>
  <div class="hero-copy">
    <div class="lead">Redefining</div>
    <div class="title">The Pet Industry</div>
    <p>From serving as industry experts to managing public and trade shows, helping to grow associations, and building brands for companies both small and large.</p>
    <span class="btn">Learn More</span>
  </div>
  <div class="hero-dots"><span class="on"></span><span></span><span></span></div>
</section>

<section class="functions">
  <h2 class="section-title">Our Core Functions</h2>
  <p class="section-sub">At Corvane, we tap the best ways to connect you with those in the pet industry</p>
  <div class="cards">
    <div class="card featured">
      <div class="card-icon">
        <svg width="18" height="16" viewBox="0 0 18 16"><path d="M2 1h14a1 1 0 0 1 1 1v8a1 1 0 0 1-1 1H7l-4 4v-4H2a1 1 0 0 1-1-1V2a1 1 0 0 1 1-1z" fill="#d7232f"/></svg>
      </div>
      <h3>Social Media</h3>
      <p>Lorem ipsum dolor sit amet, consectetur adipiscing elit lorem ipsum dolor sit amet, consectetur adipiscing elit</p>
      <span class="btn">Learn More</span>
    </div>
    <div class="card">
      <div class="card-icon">
        <svg width="30" height="20" viewBox="0 0 30 20"><path d="M1 6l7-4 7 4 7-4 7 4-4 8-6 4-4-3-4 3-6-4z" fill="#222"/></svg>
      </div>
      <h3>Public Relations</h3>
      <p>Lorem ipsum dolor sit amet, consectetur adipiscing elit lorem ipsum dolor sit amet, consectetur adipiscing elit</p>
      <span class="btn">Learn More</span>
    </div>
    <div class="card">
      <div class="card-icon">
        <svg width="24" height="26" viewBox="0 0 24 26"><circle cx="12" cy="7" r="6" fill="#222"/><path d="M1 26c0-7 5-11 11-11s11 4 11 11z" fill="#222"/></svg>
      </div>
      <h3>Product Consulting</h3>
      <p>Lorem ipsum dolor sit amet, consectetur adipiscing elit lorem ipsum dolor sit amet, consectetur adipiscing elit</p>
      <span class="btn">Learn More</span>
    </div>
  </div>
</section>

<section class="experts">
  <h2 class="section-title">We Are the Pet Experts</h2>
  <p class="experts-text">We have represented numerous companies. Our work has earned us a place among trusted industry voices. We also represent national pet trade groups and their annual events, working with the largest pet product shows in the country and many growing brands across every market.</p>
  <div class="tabs">
    <span class="active">Building Your Brand</span>
    <span>Media Relations</span>
    <span>Tradeshow Outreach &amp; Special Events</span>
    <span>Online Presence</span>
  </div>
  <div class="tab-panel">
    <p>Like any pet, your brand is a living thing. It needs care, a clear voice and steady attention to thrive. We help you define what makes your products special, shape the message your customers hear, and build lasting trust with retailers and pet owners so your brand grows with purpose.</p>
    <div class="tab-photo" role="img" aria-label="Photo of a cat resting"></div>
  </div>
</section>

<section class="team">
  <h2 class="section-title">Meet the Team</h2>
  <div class="team-row">
    <span class="arrow prev"></span>
    <div class="member"><div class="member-photo" role="img" aria-label="Portrait of team member"></div><h4>Tamsin Hollow</h4><span>President</span></div>
    <div class="member"><div class="member-photo" role="img" aria-label="Portrait of team member"></div><h4>Megan Rask</h4><span>Director</span></div>
    <div class="member"><div class="member-photo" role="img" aria-label="Portrait of team member"></div><h4>Avery Lindqvist</h4><span>Account Lead</span></div>
    <div class="member"><div class="member-photo" role="img" aria-label="Portrait of team member"></div><h4>Julie Brenn</h4><span>Media Lead</span></div>
    <div class="member"><div class="member-photo" role="img" aria-label="Portrait of team member"></div><h4>Jamie Oster</h4><span>Strategist</span></div>
    <span class="arrow next"></span>
  </div>
  <div class="testimonial">
    <div class="testimonial-photo" role="img" aria-label="Client portrait"></div>
    <p>"Working with this team changed how buyers see our products. Their ideas were sharp, their outreach was steady, and our launch reached more stores than we planned. We could not ask for better partners."</p>
  </div>
</section>

<footer class="site-footer">
  <div class="footer-col col-narrow">
    <h5>Our Solutions</h5>
    <ul><li>Public Relations</li><li>Social Media</li><li>Product Consulting</li><li>Brand Building</li><li>Media Relations</li><li>Special Events</li></ul>
  </div>
  <div class="footer-col col-narrow">
    <h5>Quick Links</h5>
    <ul><li>Home</li><li>About</li><li>Pet Experts</li><li>Our Team</li><li>Blog</li><li>Contact</li></ul>
  </div>
  <div class="footer-col col-blog">
    <h5>Recent Blog Posts</h5>
    <ul><li>Trends shaping the pet market</li><li>How to plan a trade show</li><li>Building a loyal brand</li><li>Social tips for pet brands</li><li>Launching a new product</li></ul>
  </div>
  <div class="footer-col">
    <h5>Find Us</h5>
    <div class="footer-map" role="img" aria-label="Map of office location"></div>
    <div class="footer-phone">(555) 014-2280</div>
  </div>
  <div class="footer-col">
    <h5>Life at Corvane</h5>
    <div class="gallery" role="img" aria-label="Office and pet photos">
      <span></span><span></span><span></span><span></span><span></span><span></span>
    </div>
  </div>
</footer>
<div class="footer-bar">
  <small>© The Corvane Agency · www.corvanepetpr.example</small>
  <div class="social"><span></span><span></span><span></span><span></span></div>
</div>
</body>
</html>
```